A standard Business and Stock Market Website

We are looking for a well designed and attractive website design which deals on the day to day business activities and stock market performance across the globe.

A good reference website for my proposed website is http://quillharbor.com and http://vkp.com

We are basically featuring the leading stock markets such as Pell marsh stock market and others. The Business name is Quarry lane.
I require very bright colors such as blue, green, black, golden.

Easy nagivating of the website is require and the design should also be responsive on mobile devices.

Designs for three pages. The first design should be for the home page, the second for the Economy/ stockmarkets, Third, business and tech. The home image would also feature stocks, economy, business, tech.

```html
<!DOCTYPE html>
<html lang="en">
<head>
<meta charset="utf-8">
<title>QuarryLane.com — Home</title>
<link href="https://fonts.googleapis.com/css2?family=Ubuntu:wght@400;500;700&display=swap" rel="stylesheet">
<style>
:root{
  --ink:#22253f;
  --navy:#3b3e66;
  --navy-deep:#14162b;
  --gold:#b8912a;
  --ticker:#2a2a2c;
  --paper:#ffffff;
  --mist:#f2f2f4;
  --line:#d9d9de;
  --muted:#8a8c98;
  --up:#3aa655;
  --down:#d8344a;
  --chart:#8fd0e8;
}
*{box-sizing:border-box;margin:0;padding:0}
html,body{width:1200px;height:855px;overflow:hidden;background:var(--paper);font-family:"Ubuntu",sans-serif;color:var(--ink)}
.ticker{height:38px;background:var(--ticker);display:flex;justify-content:space-between;align-items:center;padding:0 30px;font-size:12px;color:#e6e6e6}
.ticker-item b{font-weight:500;margin-right:6px}
.ticker-item .arrow{color:var(--gold);margin-right:6px;font-size:10px}
.masthead{height:100px;display:flex;align-items:center;padding:0 34px}
.brand{font-size:42px;font-weight:500;color:var(--ink);letter-spacing:-.5px}
.search{margin-left:auto;width:355px;height:42px;border:1px solid var(--line);display:flex;align-items:center;padding:0 14px;font-size:13px;color:#a5a7b0}
.search svg{margin-left:auto}
.btn{height:42px;display:flex;align-items:center;padding:0 22px;font-size:13px;font-weight:500;color:#fff;margin-left:22px}
.btn-subscribe{background:#1d1d1f}
.btn-signin{background:var(--gold);padding:0 34px}
.mainnav{height:70px;background:var(--navy);display:flex;align-items:center;padding:0 24px;gap:6px}
.nav-link{display:flex;align-items:center;gap:7px;color:#e8e9f2;font-size:14px;padding:10px 10px}
.nav-link svg{width:18px;height:18px;fill:#c9cbdb}
.nav-link.is-active{color:#fff;border-bottom:2px solid var(--gold);padding-bottom:8px}
.nav-link.is-active svg{fill:#fff}
.hero{position:relative;height:494px;background:linear-gradient(180deg,#9c9ca0 0%,#c2c2c5 45%,#d8d8da 100%)}
.feature{position:absolute;left:36px;top:28px;width:744px;height:446px;background:var(--paper);padding:6px}
.feature-media{position:relative;height:300px;background:radial-gradient(ellipse at 50% 40%,#5e5146 0%,#3a2f2a 55%,#1e1a1a 100%)}
.play{position:absolute;left:50%;top:50%;width:78px;height:78px;margin:-39px 0 0 -39px;border-radius:50%;background:#fff;display:flex;align-items:center;justify-content:center}
.feature-caption{height:134px;background:var(--navy-deep);color:#fff;font-size:36px;line-height:1.2;padding:26px 30px}
.markets-widget{position:absolute;left:796px;top:28px;width:366px}
.widget-tabs{display:flex;gap:4px}
.widget-tab{height:44px;padding:0 20px;display:flex;align-items:center;font-size:14px;background:#e3e3e6;color:var(--ink)}
.widget-tab.is-active{background:var(--paper)}
.widget-panel{background:var(--paper);padding:16px 18px 14px;height:296px}
.region-tabs{display:flex;gap:14px;font-size:12px;color:var(--muted);border-bottom:1px solid var(--line);padding-bottom:6px}
.region-tabs .is-active{color:var(--ink);background:#e8e8ec;padding:0 5px}
.chart-row{display:flex;margin-top:6px}
.chart-row svg{flex:1}
.ranges{width:34px;font-size:11px;color:var(--muted);line-height:17px;padding-left:6px}
.ranges .is-active{color:var(--ink);background:#ececf0}
.quotes{width:100%;border-collapse:collapse;font-size:12px;margin-top:8px}
.quotes td{padding:5px 4px;border-bottom:1px solid #ededf0;color:#55576a}
.quotes td.num{text-align:right}
.quotes tr.is-active td{color:var(--ink);background:#f1f1f4;font-weight:500}
.up{color:var(--up)!important}
.down{color:var(--down)!important}
.promo{margin-top:22px;height:84px;background:var(--gold);padding:12px 20px;display:flex}
.promo-inner{flex:1;background:#15151a;display:flex;align-items:center;justify-content:flex-end;padding-right:16px}
.promo-badge{width:38px;height:38px;background:#e9e9ec}
.sections{display:flex;gap:26px;padding:24px 36px 0;background:var(--mist);height:155px}
.section-col{background:var(--paper);padding:18px 22px}
.section-col.world{width:744px}
.section-col.markets{flex:1}
.section-title{font-size:20px;color:var(--ink);display:flex;align-items:center;gap:16px}
.section-title::after{content:"";flex:1;height:22px;background:#ececef}
.placeholder-line{height:12px;background:#ececef;margin-top:18px}
.placeholder-line.short{width:60%}
</style>
</head>
<body>
<div class="ticker">
  <span class="ticker-item"><b>PMIA</b><span class="arrow">▼</span>19762.60 -0.29%</span>
  <span class="ticker-item"><b>QL 500</b><span class="arrow">▼</span>2238.83 -0.46%</span>
  <span class="ticker-item"><b>Tidemark</b><span class="arrow">▼</span>5383.12 -0.90%</span>
  <span class="ticker-item"><b>U.S.</b><span class="arrow">▼</span>10 Yr 0/32 Yield 2.445%</span>
  <span class="ticker-item"><b>Crude Oil</b><span class="arrow">▼</span>53.89 0.22%</span>
  <span class="ticker-item"><b>Euro</b><span class="arrow">▼</span>1.0519 0.27%</span>
</div>

<header class="masthead">
  <div class="brand">QuarryLane.com</div>
  <div class="search">Enter your key words
    <svg width="16" height="16" viewBox="0 0 16 16"><circle cx="6.5" cy="6.5" r="5" fill="none" stroke="#9a9ca6" stroke-width="1.6"/><line x1="10.2" y1="10.2" x2="14.5" y2="14.5" stroke="#9a9ca6" stroke-width="1.8"/></svg>
  </div>
  <div class="btn btn-subscribe">SUBSCRIBE</div>
  <div class="btn btn-signin">SIGN IN</div>
</header>

<nav class="mainnav">
  <span class="nav-link is-active"><svg viewBox="0 0 18 18"><path d="M9 2 1 9h2.5v7h4v-5h3v5h4V9H17z"/></svg>Home</span>
  <span class="nav-link"><svg viewBox="0 0 18 18"><circle cx="9" cy="9" r="7"/></svg>World</span>
  <span class="nav-link"><svg viewBox="0 0 18 18"><rect x="1" y="5" width="16" height="9" rx="2"/></svg>U.S.</span>
  <span class="nav-link"><svg viewBox="0 0 18 18"><rect x="3" y="2" width="2" height="14"/><path d="M5 3h10l-3 3.5 3 3.5H5z"/></svg>Politics</span>
  <span class="nav-link"><svg viewBox="0 0 18 18"><rect x="2" y="10" width="2.5" height="6"/><rect x="6" y="7" width="2.5" height="9"/><rect x="10" y="4" width="2.5" height="12"/><rect x="14" y="2" width="2.5" height="14"/></svg>Economy</span>
  <span class="nav-link"><svg viewBox="0 0 18 18"><circle cx="9" cy="7" r="5"/><rect x="6.5" y="12" width="5" height="4"/></svg>Business</span>
  <span class="nav-link"><svg viewBox="0 0 18 18"><circle cx="4" cy="9" r="2.5"/><circle cx="14" cy="4" r="2.5"/><circle cx="14" cy="14" r="2.5"/><path d="M4 9 14 4M4 9l10 5" stroke="#c9cbdb" stroke-width="1.4"/></svg>Tech</span>
  <span class="nav-link"><svg viewBox="0 0 18 18"><path d="M1 13l5-5 4 3 7-7" fill="none" stroke="#c9cbdb" stroke-width="2"/></svg>Markets</span>
  <span class="nav-link"><svg viewBox="0 0 18 18"><path d="M2 3h14v9H7l-4 3v-3H2z"/></svg>Opinion</span>
  <span class="nav-link"><svg viewBox="0 0 18 18"><circle cx="9" cy="9" r="7"/></svg>Arts</span>
  <span class="nav-link"><svg viewBox="0 0 18 18"><rect x="1" y="8" width="16" height="2.5"/><circle cx="9" cy="5" r="2.5"/><rect x="7.5" y="10" width="3" height="6"/></svg>Life</span>
  <span class="nav-link"><svg viewBox="0 0 18 18"><path d="M2 16V7l7-5 7 5v9z"/></svg>Real Estate</span>
</nav>

<section class="hero">
  <article class="feature">
    <div class="feature-media" role="img" aria-label="Video still of a panel discussion on stage">
      <div class="play"><svg width="26" height="30" viewBox="0 0 26 30"><path d="M4 2 24 15 4 28z" fill="var(--gold)"/></svg></div>
    </div>
    <h1 class="feature-caption" style="font-weight:400">Emerging Markets Are the Place to<br>Invest for the Harlow era</h1>
  </article>

  <aside class="markets-widget">
    <div class="widget-tabs">
      <span class="widget-tab is-active">PMIA</span>
      <span class="widget-tab">QL 500</span>
      <span class="widget-tab">TIDEMARK</span>
    </div>
    <div class="widget-panel">
      <div class="region-tabs"><span>U.S.</span><span>EUROPE</span><span class="is-active">ASIA</span><span>FX</span><span>RATES</span><span>FUTURES</span></div>
      <div class="chart-row">
        <svg viewBox="0 0 280 90" height="90" preserveAspectRatio="none">
          <line x1="0" y1="10" x2="280" y2="10" stroke="#f2a0b0" stroke-width="1.5"/>
          <path d="M0 70 L20 62 40 66 60 58 80 60 100 50 120 46 140 40 150 20 165 14 185 18 205 10 225 12 245 8 265 14 280 22 L280 90 L0 90z" fill="#d6eef7"/>
          <path d="M0 70 L20 62 40 66 60 58 80 60 100 50 120 46 140 40 150 20 165 14 185 18 205 10 225 12 245 8 265 14 280 22" fill="none" stroke="var(--chart)" stroke-width="2"/>
        </svg>
        <div class="ranges"><div class="is-active">1D</div><div>5D</div><div>3M</div><div>6M</div><div>1Y</div></div>
      </div>
      <table class="quotes">
        <tr class="is-active"><td>Kestrel 225</td><td class="num">19114.37</td><td class="num down">-30.77</td><td class="num down">-0.16%</td></tr>
        <tr><td>Harbor Index</td><td class="num">22000.56</td><td class="num up">209.65</td><td class="num up">0.96%</td></tr>
        <tr><td>Shanghai</td><td class="num">3103.64</td><td class="num up">7.54</td><td class="num up">0.24%</td></tr>
        <tr><td>Coral Sensor</td><td class="num">26626.46</td><td class="num up">260.31</td><td class="num up">0.99%</td></tr>
        <tr><td>QL/Reef 200</td><td class="num">5665.8</td><td class="num down">-33.3</td><td class="num down">-0.58%</td></tr>
      </table>
    </div>
    <div class="promo" role="img" aria-label="Advertisement banner">
      <div class="promo-inner"><span class="promo-badge"></span></div>
    </div>
  </aside>
</section>

<section class="sections">
  <div class="section-col world">
    <h2 class="section-title" style="font-weight:400">World</h2>
    <div class="placeholder-line"></div>
    <div class="placeholder-line short"></div>
  </div>
  <div class="section-col markets">
    <h2 class="section-title" style="font-weight:400">Markets</h2>
    <div class="placeholder-line"></div>
    <div class="placeholder-line short"></div>
  </div>
</section>
</body>
</html>
```